依頼詳細
プロが業務用の高圧洗浄機を使い、ご自宅の外構・駐車場(ガレージ)・ブロック塀・玄関タイル・を綺麗にされたい方を募集します。
泥、排気ガスの汚れ、コケ、ほこり等を綺麗に致します。
お見積りは無料
高圧洗浄専門店
割引制度有
平日割引あり(火曜日・水曜日は特別料金にて実施)(空き状況はお電話にてご確認下さい)
施工料金等、丁寧に分かりやすくご説明します。
作業時間平均:2時間~3時間
料金:33,000円~
作業時:水道をお借りします
まずは、お気軽にご相談下さい。
株式会社ミドリノハウジング
TEL:094ー318-5562
担当:坂巻(さかまき)・梅沢(うめざわ)
営業時間:9:00~19:00

記載項目
株式会社ミドリノハウジング
094-318-5562
料金:33,000円~(範囲によって異なります)
プロの高圧洗浄はミドリノハウジングにお任せください。
サイズ
A4
ページ数
片面
希望イメージ
シンプル 複雑
単色 カラフル
暗い 明るい
日常 高級
遊び心 厳粛
未来的 伝統的
女性的 男性的
希望する色
水色系、ターコイズブルーの使用をお願い致します。
納品ファイル
• 高解像度JPG (.jpg)
補足説明
会社ロゴを添付しておりますので、ロゴの使用をお願い致します。
■ 選んだ理由

見やすく、弊社希望のチラシに近いものでした。
頂きました案件全てのチラシ案を印刷し、三つ折りにしましたが、一番良かったです。
伝えたい内容も、しっかり入っており、戸建てとなると年配の方が多いと思われ、その点でも大事な部分は文字が大きく見やすさも良く選ばせて頂きました。

■ 提案者全員のお礼・コメント

初めての依頼となりましたが、多数の応募を頂きましてありがとうございました。
正直、こんなに多数の応募を頂けるとは思ってませんでしたので驚きました。
今後もチラシの案をご依頼する事もるかと思いますので、宜しくお願い致します。

```html
<!DOCTYPE html>
<html lang="ja">
<head>
<meta charset="utf-8">
<title>外構洗浄 チラシ</title>
<link href="https://fonts.googleapis.com/css2?family=Noto+Sans+JP:wght@500;700;900&display=swap" rel="stylesheet">
<style>
:root{
  --sky:#42c3dc;
  --sky-deep:#1aa6c8;
  --navy:#0b3f73;
  --blue:#1b7fc4;
  --white:#ffffff;
  --ink:#1a1a1a;
  --yellow:#ffe23a;
  --red:#e3262f;
}
*{margin:0;padding:0;box-sizing:border-box}
html,body{width:846px;height:1200px;overflow:hidden;background:var(--white)}
body{font-family:"Noto Sans JP",sans-serif;color:var(--ink)}
.flyer{position:relative;width:846px;height:1200px;overflow:hidden;background:var(--sky)}
.bubble{position:absolute;background:var(--white);border:3px solid var(--navy);border-radius:30px;
  font-weight:900;font-size:17px;line-height:1.35;text-align:center;padding:10px 14px;color:var(--ink)}
.bubble::after{content:"";position:absolute;left:50%;width:16px;height:16px;background:var(--white);
  border-right:3px solid var(--navy);border-bottom:3px solid var(--navy);transform:translateX(-50%) rotate(45deg)}
.bubble.down::after{bottom:-10px}
.bubble.up::after{top:-10px;transform:translateX(-50%) rotate(-135deg)}
.title{position:absolute;left:0;width:100%;text-align:center;font-weight:900}
.title-main{top:268px;font-size:168px;letter-spacing:6px;color:var(--blue);line-height:1;
  -webkit-text-stroke:18px var(--white);paint-order:stroke fill}
.title-sub{top:470px;font-size:96px;line-height:1.12;color:var(--white);
  -webkit-text-stroke:14px var(--navy);paint-order:stroke fill}
.lead{position:absolute;top:836px;left:0;width:100%;text-align:center;color:var(--white);
  font-weight:900;font-size:37px;line-height:1.3;-webkit-text-stroke:7px var(--navy);paint-order:stroke fill}
.detail{position:absolute;top:930px;left:0;width:100%;text-align:center;color:var(--white);font-weight:700;font-size:17px;line-height:1.5}
.price-band{position:absolute;top:990px;left:0;width:100%;height:118px;background:var(--white)}
.estimate{position:absolute;left:20px;top:-22px;width:104px;height:104px;border-radius:50%;background:var(--yellow);
  border:3px solid var(--red);text-align:center;color:var(--red);font-weight:900;padding-top:20px}
.estimate small{display:block;font-size:15px}
.estimate strong{display:block;font-size:32px;line-height:1.1}
.worktime{position:absolute;right:60px;top:6px;font-size:17px;font-weight:700;color:var(--navy)}
.price{position:absolute;left:140px;top:20px;font-weight:900;color:var(--blue);font-size:80px;line-height:1;letter-spacing:1px}
.price .label{font-size:62px}
.discount{position:absolute;left:0;bottom:0;width:100%;height:22px;background:var(--navy);color:var(--white);
  font-size:13px;font-weight:700;line-height:22px;text-align:center}
.discount b{color:var(--yellow)}
.note{position:absolute;top:1110px;left:0;width:100%;text-align:center;font-size:12px;color:var(--white);font-weight:500}
.contact{position:absolute;top:1128px;left:0;width:100%;height:72px;background:var(--white);display:flex;align-items:center}
.brand{width:230px;display:flex;align-items:center;gap:8px;padding-left:24px;font-weight:900;font-size:17px;color:var(--blue)}
.brand i{width:16px;height:16px;background:var(--sky-deep);display:block}
.info{flex:1;padding-right:22px}
.info .cta{background:var(--sky-deep);color:var(--white);font-weight:900;font-size:19px;padding:2px 14px;border-radius:4px;margin-bottom:2px}
.info p{font-size:15px;font-weight:700;line-height:1.35;color:var(--ink)}
</style>
</head>
<body>
<main class="flyer">
  <div class="bubble down" style="left:22px;top:14px;width:240px">外構洗浄のやり方がわからない!</div>
  <div class="bubble down" style="left:300px;top:14px;width:250px">何年も外構洗浄をしたことが無い!</div>
  <div class="bubble down" style="left:590px;top:14px;width:236px">ブロック塀ってキレイになるの?</div>
  <div class="bubble down" style="left:22px;top:104px;width:240px">駐車場の土などのコケや汚れが気になってきた…</div>
  <div class="bubble down" style="left:300px;top:118px;width:250px">最近、玄関のタイルの汚れが気になる!</div>
  <div class="bubble down" style="left:590px;top:104px;width:236px">家のコケを落とせるけどどうしたらいいの?</div>

  <h1 class="title title-main">外構洗浄</h1>
  <p class="title title-sub">お困りでは<br>ありませんか?</p>

  <div class="bubble up" style="left:22px;top:708px;width:240px">高圧洗浄って傷が付いたりしないの?</div>
  <div class="bubble up" style="left:300px;top:720px;width:250px">ガレージもキレイにしたい!</div>
  <div class="bubble up" style="left:590px;top:708px;width:236px">頼んでみたいけどプロに頼むと高そう…</div>

  <p class="lead">そんな時は高圧洗浄のプロ、<br>ミドリノハウジングにお任せください。</p>
  <p class="detail">ご自宅の外構・駐車場(ガレージ)・ブロック塀、玄関タイル、泥、<br>排気ガスの汚れ、コケ、ほこり等を綺麗に致します。</p>

  <section class="price-band">
    <div class="estimate"><small>お見積り</small><strong>無料</strong></div>
    <p class="worktime">作業時間平均 2～3時間</p>
    <p class="price"><span class="label">料金</span>33,000円~</p>
    <p class="discount"><b>平日割引あり</b>(火曜日・水曜日は特別料金にて実施) ※空き状況はお電話にてご確認下さい</p>
  </section>
  <p class="note">※料金は範囲によって異なります。作業時は水道をお借りします。</p>

  <footer class="contact">
    <div class="brand"><i></i>ミドリノハウジング</div>
    <div class="info">
      <p class="cta">まずは、お気軽にご相談ください。</p>
      <p>株式会社ミドリノハウジング</p>
      <p>TEL:094ー318-5562 営業時間:9:00~19:00　担当:坂巻(さかまき)・梅沢(うめざわ)</p>
    </div>
  </footer>
</main>
</body>
</html>
```